Freelance yoga teacher looking for professional postcard design

I need a postcard that shows my class times & venues. I also would like it to show that I offer private one to one sessions for those not ready for group practice, or who require personal attention. It needs to show my contact details - mob: 07344120588, email & website addresses. I also want the opportunity to add other services in future, such as my website and yoga massage.

UPDATE 18 JULY

FRONT OF POSTCARD
I would like the front side of the postcard to not look too busy or 'wordy'. If using bullet points, be creative, so no ticks. Please use my full name Maren T Holloway NCM Dip.

REVERSE SIDE
The reverse side I think should have the National Circle of Movement, together with words describing classes, 'classes are designed...' please omit the sentences starting 'by running courses...'

'Postage required' or lines for an address are not required.

Make the 'where I teach' venues/times look personable, so no harsh gridlines please.

Target Market(s)

Most of my students are 30+ professionals with disposable income or early retirees.

Industry/Entity Type

Teacher

Requirements
Must have
• It must show my National Circle of Movement Teacher Logo which I can supply.
Maren T Holloway is a National Circle of Movement trained teacher.
Classes are small and friendly, designed to create ease in the body, reduce stress and promote relaxation. Julie is passionate about sharing yoga, respecting each individual and modifying to suit their needs, leading to improved function, mobility and stability.

Keep any images simple, such as rolled up yoga mats. I am commissioning a personal mandala which I will use as a logo, but this will not be ready until mid to late August.

Please see attached 'attempt' at a postcard giving details of classes/venues, contact info.
Nice to have
• Somewhere on the postcard the words: 'Yoga. Centre the body & mind. Stretch the possibilities.'
Should not have
• Images of people doing yoga or silhouettes of yoga postures.

```html
<!DOCTYPE html>
<html lang="en">
<head>
<meta charset="utf-8">
<title>Postcard reverse – where I teach</title>
<link rel="stylesheet" href="https://fonts.googleapis.com/css2?family=Questrial&display=swap">
<style>
  :root {
    --leaf: #23653a;
    --leaf-soft: #e8f1ea;
    --leaf-line: #b9d3c0;
    --ink: #1a1a1a;
    --paper: #ffffff;
  }
  * { box-sizing: border-box; }
  html, body {
    margin: 0;
    padding: 0;
    overflow: hidden;
    background: var(--paper);
  }
  .postcard {
    position: relative;
    width: 1200px;
    height: 930px;
    overflow: hidden;
    background: var(--paper);
    font-family: "Questrial", "Century Gothic", sans-serif;
    color: var(--ink);
  }

  /* Class timetable – soft, no hard grid */
  .timetable {
    position: absolute;
    left: 45px;
    top: 44px;
    width: 621px;
    border-collapse: separate;
    border-spacing: 0;
    table-layout: fixed;
  }
  .timetable th,
  .timetable td { padding: 0; }
  .timetable thead tr { height: 43px; }
  .timetable th {
    background: var(--leaf);
    color: var(--paper);
    font-weight: 400;
    font-size: 26px;
    letter-spacing: 0.5px;
  }
  .timetable th:first-child { border-radius: 14px 0 0 0; }
  .timetable th:last-child { border-radius: 0 14px 0 0; }
  .col-location { width: 269px; }
  .col-day { width: 169px; }
  .col-time { width: 183px; }
  .timetable tbody tr { height: 42px; }
  .timetable tbody td { border-bottom: 1px dotted var(--leaf-line); }
  .timetable tbody tr.venue-end td,
  .timetable tbody td.venue { border-bottom: 2px solid var(--leaf-line); }
  .timetable tbody tr:last-child td { border-bottom: none; }
  .group-alt td { background: var(--leaf-soft); }
  .venue {
    vertical-align: top;
    font-size: 17px;
    line-height: 22px;
    padding: 12px 8px 0 13px !important;
    letter-spacing: 0.3px;
  }
  .venue--tight { padding-top: 3px !important; }
  .venue--community { padding-top: 10px !important; }
  .day {
    font-size: 17px;
    padding-left: 10px !important;
    letter-spacing: 0.3px;
  }
  .day--lead { font-size: 23px; }
  .time {
    font-size: 17px;
    padding-left: 11px !important;
    letter-spacing: 0.2px;
  }
  .time--split {
    text-align: center;
    line-height: 22px;
    padding-left: 0 !important;
    padding-bottom: 8px !important;
  }
  .timetable tbody tr.row-community { height: 125px; }
  .timetable .row-community td { border-radius: 0; }

  /* Contact */
  .contact {
    position: absolute;
    left: 45px;
    top: 437px;
    width: 620px;
    text-align: center;
    color: var(--leaf);
    font-size: 21px;
    line-height: 25px;
    letter-spacing: 1px;
  }
  .contact p { margin: 0; }

  /* Teacher mark, top right */
  .teacher-mark {
    position: absolute;
    left: 900px;
    top: 40px;
    width: 260px;
    display: flex;
    flex-direction: column;
    align-items: center;
    text-align: center;
    color: var(--leaf);
  }
  .teacher-mark__dot {
    width: 96px;
    height: 96px;
    border-radius: 50%;
    background: var(--leaf);
    margin-bottom: 14px;
  }
  .teacher-mark__name {
    font-size: 22px;
    line-height: 28px;
    letter-spacing: 0.5px;
  }

  /* One to one sessions */
  .private-sessions {
    position: absolute;
    left: 735px;
    top: 300px;
    width: 425px;
    text-align: center;
    color: var(--leaf);
  }
  .private-sessions h2 {
    margin: 0 0 10px;
    font-weight: 400;
    font-size: 26px;
    letter-spacing: 0.5px;
  }
  .private-sessions p {
    margin: 0;
    font-size: 17px;
    line-height: 24px;
    color: var(--ink);
  }

  .website {
    position: absolute;
    left: 735px;
    top: 462px;
    width: 425px;
    text-align: center;
    color: var(--leaf);
    font-size: 21px;
    letter-spacing: 1px;
    margin: 0;
  }

  .meadow-band {
    position: absolute;
    left: 30px;
    top: 690px;
    width: 1140px;
    height: 210px;
  }
</style>
</head>
<body>
<main class="postcard">
  <table class="timetable">
    <colgroup>
      <col class="col-location"><col class="col-day"><col class="col-time">
    </colgroup>
    <thead>
      <tr><th>Location</th><th>Day</th><th>Time</th></tr>
    </thead>
    <tbody>
      <tr>
        <td class="venue" rowspan="3">The Meadow Hall,<br>Linden Road, Ashby Vale,<br>AV12 4RT</td>
        <td class="day day--lead">Monday</td>
        <td class="time">1:45pm - 3:00pm</td>
      </tr>
      <tr>
        <td class="day">Tuesday</td>
        <td class="time">5:00pm - 6:15pm</td>
      </tr>
      <tr class="venue-end">
        <td class="day">Thursdays</td>
        <td class="time">6:15pm - 7:30pm</td>
      </tr>
      <tr class="group-alt">
        <td class="venue venue--tight" rowspan="2">Willow Trust,<br>Hawthorn Court, Elmsworth,<br>AV14 6JN</td>
        <td class="day">Monday</td>
        <td class="time">6:30pm - 8:00pm</td>
      </tr>
      <tr class="group-alt venue-end">
        <td class="day">Tuesday</td>
        <td class="time">10:15am-11:30am</td>
      </tr>
      <tr class="row-community">
        <td class="venue venue--community">ACVS (Ashby Commu-<br>nity &amp; Voluntary Service),<br>Millbrook Road, Kestwick,<br>KW8 3LP</td>
        <td class="day">Wednesday</td>
        <td class="time time--split">5:30pm - 7:00pm<br>&amp;<br>7:30pm - 8:45pm</td>
      </tr>
    </tbody>
  </table>

  <div class="contact">
    <p class="contact-name">Maren T Holloway NCM Dip</p>
    <p class="contact-phone">Phone: 07344120588</p>
    <p class="contact-email">E-mail: maren.t.holloway@mailnetcom</p>
  </div>

  <div class="teacher-mark">
    <span class="teacher-mark__dot"></span>
    <span class="teacher-mark__name">National Circle of Movement<br>Trained Teacher</span>
  </div>

  <section class="private-sessions">
    <h2>Private one to one sessions</h2>
    <p>For those not yet ready for group practice,<br>or who would like personal attention.</p>
  </section>

  <p class="website">www.marenholloway-yoga.co.uk</p>

  <svg class="meadow-band" viewBox="0 0 1140 210" role="img" aria-label="Green silhouette of grass and wild flowers along the bottom edge">
    <path fill="#23653a" d="M0 95 C120 60 220 110 330 95 C450 78 520 60 640 88 C760 112 860 70 980 82 C1060 90 1110 75 1140 85 L1140 210 L0 210 Z"/>
  </svg>
</main>
</body>
</html>
```